Halvercott Orthodontics business card

Using our existing logo (created with ArtFolio), please create a tasteful, contemporary business card. We are father and daughter orthodontists specializing in braces, clarafit, etc to design healthy, beautiful smiles for children, adolescents, and adults. We would like the design to be family-friendly but not childish.
The final design should include all of the information without looking cluttered (I hope! If necessary to achieve an optimal design, please consider making the card double-sided)
Purple, black, silver on a white card
Please include the following information:
Halvercott Orthodontics (logo)
Marguerite L. Halvercott, DMD
Douglas R. Halvercott, DMD

312 Bramblewood Street
North Andover, MA 01899
978.555.0142

847C Quarry Hollow Street
Methuen, MA 01898
978.555.0187

email frontdesk@halvercottortho.example
website www.halvercottortho.example

```html
<!DOCTYPE html>
<html lang="en">
<head>
<meta charset="utf-8">
<title>Halvercott Orthodontics – Business Card</title>
<link rel="stylesheet" href="https://fonts.googleapis.com/css2?family=Outfit:wght@400;500;600&display=swap">
<style>
  :root {
    --purple: #652f8c;
    --white: #ffffff;
    --backdrop: #eceef1;
    --card-shadow: rgba(30, 30, 50, 0.18);
  }
  * { margin: 0; padding: 0; box-sizing: border-box; }
  html, body {
    width: 1200px; height: 1200px; overflow: hidden;
    background: var(--backdrop);
    font-family: "Outfit", sans-serif;
  }
  .stage { position: relative; width: 1200px; height: 1200px; }
  .card {
    position: absolute; left: 253px; width: 694px; height: 393px;
    background: var(--white);
    box-shadow: 0 10px 30px var(--card-shadow);
    overflow: hidden;
  }
  .card--front { top: 168px; }
  .card--back { top: 639px; }

  .brand {
    display: flex; align-items: center; gap: 12px;
    color: var(--purple); font-weight: 600; letter-spacing: 0.5px;
    white-space: nowrap;
  }
  .brand__dot {
    width: 18px; height: 18px; border-radius: 50%; background: var(--purple);
  }

  /* Front */
  .front__brand {
    position: absolute; top: 38px; left: 0; right: 0;
    justify-content: center; font-size: 36px;
  }
  .doctors {
    position: absolute; top: 124px; left: 0; right: 0;
    display: flex; justify-content: center;
  }
  .doctor {
    color: var(--purple); font-size: 27px; font-weight: 400; line-height: 1.2;
    padding: 0 18px;
  }
  .doctor + .doctor { border-left: 2px solid var(--purple); }
  .contact-band {
    position: absolute; top: 222px; left: 0; right: 0; height: 144px;
    background: var(--purple); color: var(--white);
    display: flex; flex-direction: column; justify-content: center; align-items: center;
    gap: 11px; font-size: 18px; font-weight: 400;
  }
  .stripe { position: absolute; left: 0; right: 0; background: var(--purple); }
  .front__stripe-a { top: 372px; height: 6px; }
  .front__stripe-b { top: 386px; height: 7px; }

  /* Back */
  .back__stripe-top { top: 12px; height: 12px; }
  .back__stripe-bottom { top: 365px; height: 12px; }
  .logo-bar {
    position: absolute; top: 168px; left: 0; right: 0; height: 57px;
    display: flex; align-items: center;
  }
  .logo-bar__rule { flex: 1; height: 57px; background: var(--purple); }
  .logo-bar .brand {
    font-size: 40px; padding: 0 20px; background: var(--white); height: 100%;
  }
</style>
</head>
<body>
  <main class="stage">
    <section class="card card--front" aria-label="Business card front">
      <div class="brand front__brand">
        <span class="brand__dot"></span>
        <span class="brand__name">Halvercott Orthodontics</span>
      </div>
      <div class="doctors">
        <p class="doctor">Marguerite L. Halvercott<br>DMD</p>
        <p class="doctor">Douglas R. Halvercott<br>DMD</p>
      </div>
      <div class="contact-band">
        <span class="contact__address">312 Bramblewood Street, North Andover, MA 01899</span>
        <span class="contact__phone">978.555.0142</span>
        <span class="contact__email">frontdesk@halvercottortho.example</span>
        <span class="contact__web">www.halvercottortho.example</span>
      </div>
      <div class="stripe front__stripe-a"></div>
      <div class="stripe front__stripe-b"></div>
    </section>

    <section class="card card--back" aria-label="Business card back">
      <div class="stripe back__stripe-top"></div>
      <div class="logo-bar">
        <div class="logo-bar__rule"></div>
        <div class="brand">
          <span class="brand__dot"></span>
          <span class="brand__name">Halvercott Orthodontics</span>
        </div>
        <div class="logo-bar__rule"></div>
      </div>
      <div class="stripe back__stripe-bottom"></div>
    </section>
  </main>
</body>
</html>
```